Tarvel Ridge LLC

Need Professional Business cards for New Investment Fund

Target Market(s)

High Quality investors

Industry/Entity Type

Financial

Contact Information for Business Card

Phone Number +1 555 284 6193
Name Pavel Orlinsky
Title Fund Manager
email po@FundTarvel.example
Website www.FundTarvel.example

Colors

Designer to choose colors to be used in the design.

Requirements
Must have
• Must have our Logo and all of the above. Must be made so lettering and loge can be raised

```html
<!DOCTYPE html>
<html lang="en">
<head>
<meta charset="utf-8">
<title>Tarvel Ridge – Business Card</title>
<link rel="stylesheet" href="https://fonts.googleapis.com/css2?family=Jost:wght@500;600&family=Roboto:wght@400&family=Didact+Gothic&display=swap">
<style>
  :root {
    --page-bg: #e9e9ea;
    --card-dark: #1f1f20;
    --accent-green: #cfe07e;
    --text-light: #ffffff;
    --text-dark: #1f1f20;
  }
  * { margin: 0; padding: 0; box-sizing: border-box; }
  html, body {
    width: 1200px; height: 1200px; overflow: hidden;
    background: var(--page-bg);
  }
  .canvas {
    width: 1200px; height: 1200px;
    display: flex; align-items: center; justify-content: center;
  }
  .business-card {
    position: relative;
    width: 960px; height: 548px;
    background: var(--card-dark);
    box-shadow: 0 10px 30px rgba(0,0,0,0.18);
    overflow: hidden;
  }
  .brand-panel {
    position: absolute; top: 0; right: 0;
    width: 270px; height: 100%;
    background: var(--accent-green);
    display: flex; flex-direction: column; justify-content: center; align-items: center;
  }
  .brand-name {
    font-family: "Jost", sans-serif;
    font-weight: 600;
    font-size: 42px;
    line-height: 1.05;
    letter-spacing: 1px;
    color: var(--text-dark);
    text-align: center;
    text-transform: uppercase;
  }
  .identity {
    position: absolute; left: 345px; top: 195px;
    transform: translateX(-50%);
    text-align: center;
  }
  .person-name {
    display: inline-block;
    font-family: "Jost", sans-serif;
    font-weight: 600;
    font-size: 44px;
    color: var(--text-light);
    padding-bottom: 4px;
    border-bottom: 2px solid var(--accent-green);
    white-space: nowrap;
  }
  .person-title {
    font-family: "Roboto", sans-serif;
    font-weight: 400;
    font-size: 31px;
    color: var(--text-light);
    margin-top: 6px;
  }
  .contact-list {
    position: absolute; left: 46px; top: 386px;
    list-style: none;
  }
  .contact-item {
    display: flex; align-items: center;
    height: 44px;
    font-family: "Didact Gothic", sans-serif;
    font-size: 25px;
    color: var(--text-light);
    letter-spacing: 0.5px;
  }
  .contact-icon {
    width: 22px; height: 22px; margin-right: 22px; flex: none;
  }
</style>
</head>
<body>
<main class="canvas">
  <section class="business-card">
    <div class="identity">
      <h1 class="person-name">Pavel Orlinsky</h1>
      <p class="person-title">Fund Manager</p>
    </div>

    <ul class="contact-list">
      <li class="contact-item">
        <svg class="contact-icon" viewBox="0 0 22 22" aria-hidden="true">
          <rect width="22" height="22" rx="3" fill="var(--accent-green)"/>
          <path d="M7 5c-1 1-1.5 2-1 4 1 3 4 6.5 7 7.5 2 .5 3 0 4-1l-2.5-2.5-1.5 1c-1.5-.5-3.5-2.5-4-4l1-1.5z" fill="var(--card-dark)"/>
        </svg>
        +1 555 284 6193
      </li>
      <li class="contact-item">
        <svg class="contact-icon" viewBox="0 0 22 22" aria-hidden="true">
          <rect width="22" height="22" rx="3" fill="var(--accent-green)"/>
          <rect x="4" y="6" width="14" height="10" fill="none" stroke="var(--card-dark)" stroke-width="1.5"/>
          <path d="M4 6l7 6 7-6M4 16l5-5M18 16l-5-5" fill="none" stroke="var(--card-dark)" stroke-width="1.5"/>
        </svg>
        po@FundTarvel.example
      </li>
      <li class="contact-item">
        <svg class="contact-icon" viewBox="0 0 22 22" aria-hidden="true">
          <rect width="22" height="22" rx="3" fill="var(--accent-green)"/>
          <circle cx="11" cy="11" r="6.5" fill="none" stroke="var(--card-dark)" stroke-width="1.4"/>
          <ellipse cx="11" cy="11" rx="3" ry="6.5" fill="none" stroke="var(--card-dark)" stroke-width="1.2"/>
          <path d="M4.5 11h13M5.5 8h11M5.5 14h11" stroke="var(--card-dark)" stroke-width="1.2"/>
        </svg>
        www.FundTarvel.example
      </li>
    </ul>

    <div class="brand-panel">
      <p class="brand-name">Tarvel<br>Ridge</p>
    </div>
  </section>
</main>
</body>
</html>
```